Business Card Design

We need a new buisness card designed for a new company in Darwin
We dig trenchs and lay pipes for the communication industry,Electrical industry, Teleco industry,
We also do some concrete works as well,
And small excavation work
Communication
Belvanti Contracting PTY LTD
Pit and Pipe installations
Trenching,Excavations, Concreting ,
civil works, unistrut soloutions ,over thirty years experiance
WHERE NOT FAZED WE WILL LAY ANYTHING
Contact Glen 0491536208 ps
(would like name to stand out somehow in another text or graphic sort of a way am also looking for some sort of slogan) will most likely be a red card with black writing

```html
<!DOCTYPE html>
<html lang="en">
<head>
<meta charset="UTF-8">
<title>Belvanti Contracting PTY LTD – Business Card</title>
<link rel="stylesheet" href="https://fonts.googleapis.com/css2?family=Alfa+Slab+One&family=Arimo:wght@700&family=Andika&display=swap">
<style>
  :root {
    --red-deep: #c4000b;
    --red-mid: #dd1c22;
    --red-light: #f04c4f;
    --ink: #2f2a2a;
    --white: #ffffff;
  }
  html, body {
    margin: 0;
    padding: 0;
    overflow: hidden;
    background: #ffffff;
  }
  .card {
    position: relative;
    width: 1200px;
    height: 686px;
    overflow: hidden;
    background: radial-gradient(ellipse 65% 70% at 50% 45%, var(--red-light) 0%, var(--red-mid) 45%, var(--red-deep) 100%);
    font-family: "Arimo", Arial, sans-serif;
    color: var(--ink);
  }
  .brand {
    position: absolute;
    left: 0;
    top: 88px;
    width: 1210px;
    text-align: center;
  }
  .brand-name {
    margin: 0;
    font-family: "Alfa Slab One", "Rockwell", serif;
    font-weight: 400;
    font-size: 55px;
    line-height: 1;
    letter-spacing: 0.5px;
    color: var(--ink);
  }
  .brand-suffix {
    position: absolute;
    left: 343px;
    top: 144px;
    width: 522px;
    display: flex;
    align-items: center;
    gap: 8px;
  }
  .brand-suffix .rule {
    flex: 1;
    height: 2px;
    background: var(--ink);
  }
  .brand-suffix .suffix-text {
    font-weight: 700;
    font-size: 23px;
    line-height: 1;
    letter-spacing: 0.5px;
    color: var(--ink);
  }
  .services {
    position: absolute;
    left: 46px;
    top: 229px;
    margin: 0;
    padding: 0;
    list-style: none;
  }
  .services li {
    display: flex;
    align-items: center;
    height: 22px;
    margin-bottom: 24px;
    font-weight: 700;
    font-size: 25px;
  }
  .services li:last-child { margin-bottom: 0; font-size: 24px; }
  .services .box {
    width: 17px;
    height: 17px;
    margin-right: 4px;
    background: var(--white);
    border: 2px solid var(--ink);
    box-sizing: border-box;
    border-radius: 2px;
  }
  .experience {
    position: absolute;
    left: 95px;
    top: 359px;
    margin: 0;
    font-weight: 700;
    font-size: 30px;
    line-height: 1;
    color: var(--ink);
  }
  .slogan {
    position: absolute;
    left: 0;
    top: 428px;
    width: 1237px;
    margin: 0;
    text-align: center;
    font-family: "Alfa Slab One", "Rockwell", serif;
    font-weight: 400;
    font-size: 27px;
    line-height: 1;
    letter-spacing: 0.4px;
    color: var(--ink);
  }
  .contact {
    position: absolute;
    left: 450px;
    top: 545px;
    color: var(--white);
  }
  .contact .phone-icon {
    position: absolute;
    left: 0;
    top: 8px;
    width: 62px;
    height: 78px;
  }
  .contact .contact-name {
    position: absolute;
    left: 50px;
    top: 0;
    margin: 0;
    white-space: nowrap;
    font-weight: 700;
    font-size: 34px;
    line-height: 1;
  }
  .contact .contact-number {
    position: absolute;
    left: 77px;
    top: 40px;
    margin: 0;
    white-space: nowrap;
    font-family: "Andika", "Trebuchet MS", sans-serif;
    font-size: 46px;
    line-height: 1;
    letter-spacing: 1px;
  }
</style>
</head>
<body>
  <main class="card">
    <header>
      <div class="brand">
        <h1 class="brand-name">Belvanti Contracting</h1>
      </div>
      <div class="brand-suffix">
        <span class="rule"></span>
        <span class="suffix-text">PTY LTD</span>
        <span class="rule"></span>
      </div>
    </header>

    <ul class="services">
      <li><span class="box"></span>Pit and Pipe installations Trenching</li>
      <li><span class="box"></span>Excavations</li>
      <li><span class="box"></span>concreting civil works</li>
    </ul>

    <p class="experience">over thirty years experiance</p>

    <p class="slogan">WHERE NOT FAZED WE WILL LAY ANYTHING</p>

    <section class="contact">
      <svg class="phone-icon" viewBox="0 0 62 78" aria-hidden="true">
        <g fill="none" stroke="#ffffff" stroke-width="4" stroke-linecap="round">
          <path d="M30 52 C 18 58, 10 62, 6 68 C 3 73, 8 77, 14 74 C 20 70, 14 64, 9 70"/>
          <path d="M14 74 C 24 76, 40 72, 52 72"/>
        </g>
        <g fill="#ffffff">
          <rect x="6" y="4" width="14" height="20" rx="3" transform="rotate(-35 13 14)"/>
          <rect x="30" y="36" width="14" height="20" rx="3" transform="rotate(-35 37 46)"/>
          <path d="M12 20 L 20 16 L 38 40 L 30 46 Z"/>
        </g>
      </svg>
      <p class="contact-name">Contact Glen</p>
      <p class="contact-number">0491536208</p>
    </section>
  </main>
</body>
</html>
```